How To Guide for Licensing Pet

3.5" x 2.5" playing card size. Two sided design, color is alright. Front side, City of Davenport Pet License, and back side would be City of Kestrelton Dog License.
*Note both cities have different licensing requirements, dates and pricing.

Local License Fees
The City of Davenport requires that all dogs and cats be licensed over the age of 6 months. Pet owners must purchase a license for their pet within thirty days of the date the pet is initially given the rabies vaccine and annually within thirty days’ time of the date of the current rabies vaccination. Licenses can be purchased at the Animal Rescue League of Marlow Hollow with verification of a current rabies vaccination signed and administered by a licensed veterinarian.

Annual license fees are:

Neutered/spayed (altered) dog or cat – $10
Non-altered dog or cat – $30

To License: Current identification & current rabies vaccination certificate and bring to Animal Rescue League of Marlow Hollow
4417 E Birchmont Hill Rd
Harrowgate, IA 50999
555-014-2298

-
The City of Kestrelton requires every dog over 6 months of age be licensed. Licenses can be purchased at the Animal Rescue League of Marlow Hollow . Pet licenses must be purchased prior to January 31 of each calendar year. Pet owners applying for a license must present a certificate of current rabies vaccination signed and administered by a licensed veterinarian.

Annual license fees are:

Neutered/spayed (altered) dog – $3
Non-altered dog – $25

4417 E Birchmont Hill Rd
Harrowgate, IA 50999
555-014-2298

Target Market(s)

Animal Owners, easy to read

Industry/Entity Type

Pet

Requirements
Must have
• SIZE: 3.5" x 2.5" Playing Card Size
2 sides, Front: Davenport, Back: Bettendorf.
Bettendorf only has Dog License requirement*

```html
<!DOCTYPE html>
<html lang="en">
<head>
<meta charset="utf-8">
<title>City of Kestrelton Dog License</title>
<link rel="stylesheet" href="https://fonts.googleapis.com/css2?family=Arimo:wght@700&display=swap">
<style>
  :root {
    --ink: #1f1f1c;
    --glow: rgba(255, 255, 255, 0.85);
    --field-light: #d7dab3;
    --field-mid: #c4c99a;
    --coat-warm: #b3a584;
    --coat-deep: #9a8c70;
  }
  html, body {
    margin: 0;
    padding: 0;
    width: 1200px;
    height: 857px;
    overflow: hidden;
    background: #ffffff;
  }
  .license-card {
    position: relative;
    width: 1200px;
    height: 857px;
    overflow: hidden;
    font-family: "Arimo", Arial, sans-serif;
    font-weight: 700;
    color: var(--ink);
  }
  .backdrop {
    position: absolute;
    inset: 0;
  }
  .card-text {
    position: absolute;
    inset: 0;
    text-shadow: 0 0 3px var(--glow), 1px 1px 2px var(--glow), -1px -1px 2px var(--glow);
  }
  .card-title {
    position: absolute;
    top: 42px;
    left: 0;
    width: 100%;
    margin: 0;
    text-align: center;
    font-size: 50px;
    letter-spacing: 5px;
  }
  .intro {
    position: absolute;
    top: 118px;
    left: 43px;
    width: 1130px;
    margin: 0;
    font-size: 24px;
    line-height: 37px;
    letter-spacing: 3.5px;
    white-space: nowrap;
  }
  .intro .indent { padding-left: 46px; }
  .section-heading {
    position: absolute;
    left: 43px;
    margin: 0;
    font-size: 35px;
    letter-spacing: 5px;
  }
  .fees-heading { top: 354px; }
  .how-heading { top: 510px; }
  .fee-list {
    position: absolute;
    top: 425px;
    left: 43px;
    margin: 0;
    padding: 0;
    list-style: none;
    font-size: 24px;
    line-height: 37px;
    letter-spacing: 3.5px;
  }
  .how-to {
    position: absolute;
    top: 581px;
    left: 43px;
    margin: 0;
    font-size: 24px;
    line-height: 37.5px;
    letter-spacing: 3.5px;
    white-space: nowrap;
  }
  .office-address {
    position: absolute;
    top: 656px;
    left: 89px;
    margin: 0;
    font-style: normal;
    font-size: 24px;
    line-height: 37.5px;
    letter-spacing: 3.5px;
  }
</style>
</head>
<body>
<main class="license-card">
  <svg class="backdrop" width="1200" height="857" viewBox="0 0 1200 857" role="img" aria-label="Softly faded photograph of a brindle dog in profile wearing a harness, set against a sunlit grassy field">
    <defs>
      <linearGradient id="scene-tone" x1="0" y1="0" x2="1" y2="0.3">
        <stop offset="0" stop-color="var(--coat-deep)"/>
        <stop offset="0.35" stop-color="var(--coat-warm)"/>
        <stop offset="0.7" stop-color="var(--field-mid)"/>
        <stop offset="1" stop-color="var(--field-light)"/>
      </linearGradient>
    </defs>
    <rect width="1200" height="857" fill="url(#scene-tone)"/>
  </svg>

  <section class="card-text">
    <h1 class="card-title">City of Kestrelton</h1>
    <p class="intro"><span class="indent">The City of Kestrelton requires every dog over 6 months of age be</span><br>licensed. Licenses can be purchased at the Animal Rescue League of<br>Marlow Hollow or from Kestrelton City Hall. Pet licenses must be<br>purchased prior to January 31 of each calendar year. Pet owners<br>applying for a license must present a certificate of current rabies<br>vaccination signed and administered by a licensed veterinarian.</p>

    <h2 class="section-heading fees-heading">Annual license fees:</h2>
    <ul class="fee-list">
      <li>Neutered/spayed (altered) dog – $3</li>
      <li>Non-altered dog – $25</li>
    </ul>

    <h2 class="section-heading how-heading">To License:</h2>
    <p class="how-to">Current identification &amp; current rabies vaccination certificate and<br>bring to Animal Rescue League of Marlow Hollow</p>
    <address class="office-address">4417 E Birchmont Hill Rd<br>Harrowgate, IA 50999<br>(555) 014-2298</address>
  </section>
</main>
</body>
</html>
```